"Tarvel Mouthguards " Custom-made Mouthguard Business Website

We need an informational website for our mouthguard Business "Tarvel Mouthguards". The logo is navy blue/lime green so want to have colour scheme that goes nicely with this - have uploaded our mouthguard flyer with some information we need to put into the website but I do have more information to put in there.

Target Market(s)

Sports clubs, sportspeople, parents and kids, schools

Industry/Entity Type

Dental, Custom-made Sports Mouthguards

Coding

Number of Pages Required

5+ page

Font styles to use
Serif
Sans Serif

Colors
0054AA
0677BA
7BADD7
CADEEF
E8F1F8
0094D4
00A9DD
6FCCEA
C7EBF8
E9F6FB
00AB8E
00BBA5
67D7C9
C6EFE9
E9F9F6
59FF00
82FF00
B8FF75
E3FFCB
F4FFEA
FFF300
FFF600
FEFA6F
FFFEC7
FFFEE8
FFC000
F8CF3A
FAE287
FDF2CF
FEFAEE
F0912C
F2A743
F7CA91
FBE8D2
FDF5EE
EE7325
F08F49
F5BC92
FAE3D3
FDF4ED

Requirements
Must have
• I want drop down pages, not one scrolling page. Different pages for each heading . Content uploaded - We need a general home page with lots of pictures and info that I'll provide. A page each dedicated to 1) About Us 2) Why choose a custom mouthguard? 3) Gallery 4) Contact Us. Will need logos from "Morvex"
Nice to have
• Mainly use greens and blues, but happy to pop in some yellow/oranges/red oranges if it looks good

```html
<!DOCTYPE html>
<html lang="en">
<head>
<meta charset="utf-8">
<title>Tarvel Mouthguards – Custom-Made Sports Mouthguards In Perth</title>
<link href="https://fonts.googleapis.com/css2?family=Oswald:wght@500;600;700&family=Poppins:wght@400;500;600;700&display=swap" rel="stylesheet">
<style>
:root{
  --navy:#0c2b6b;
  --navy-deep:#08214f;
  --green:#3fcf2f;
  --lime:#59ff00;
  --white:#ffffff;
  --ink:#1d2333;
  --muted:#4a5063;
  --pale:#eef2f7;
  --blue:#0094d4;
  --orange:#f0912c;
  --yellow:#ffc000;
  --pink:#f0406e;
}
*{box-sizing:border-box;margin:0;padding:0}
html,body{width:1200px;height:4525px;overflow:hidden}
body{position:relative;background:var(--white);font-family:'Poppins',sans-serif;color:var(--ink)}
.abs{position:absolute}
.heading{font-family:'Oswald',sans-serif;font-weight:700;text-transform:uppercase;letter-spacing:.5px;text-align:center}
.heading.navy{color:var(--navy)}
.heading.green{color:var(--green)}
.btn{position:absolute;display:flex;align-items:center;justify-content:center;border-radius:5px;font-family:'Poppins',sans-serif;font-weight:700;font-size:11px;text-transform:uppercase;letter-spacing:.3px}
.btn.light{background:var(--white);color:var(--navy);box-shadow:0 2px 6px rgba(0,0,0,.2)}
.btn.dark{background:var(--navy);color:var(--white)}
.photo{position:absolute}

/* header */
.site-header{position:absolute;left:0;top:0;width:1200px;height:74px;background:var(--white);z-index:5}
.brand{position:absolute;left:123px;top:14px;color:var(--navy);font-family:'Poppins',sans-serif;font-weight:700;line-height:1}
.brand .name{font-size:22px;letter-spacing:.5px}
.brand .tag{font-size:6px;color:var(--green);margin-top:3px;letter-spacing:.4px;text-transform:uppercase;font-weight:500}
.nav{position:absolute;left:337px;top:30px;display:flex;gap:25px;font-size:10px;font-weight:600;text-transform:uppercase;color:var(--navy)}
.nav .active{color:var(--green)}
.nav-icon{position:absolute;top:22px;width:30px;height:30px;border-radius:50%;background:var(--navy)}
.quick{left:950px;top:19px;width:125px;height:37px;font-size:11px}

/* hero */
.hero-text{left:144px;top:170px;color:var(--white)}
.hero-brand{font-family:'Poppins',sans-serif;font-weight:700;font-size:27px;color:var(--green);line-height:1.05;letter-spacing:1px;text-transform:uppercase}
.hero-title{font-family:'Oswald',sans-serif;font-weight:600;font-size:28px;line-height:1.3;margin-top:22px;text-transform:capitalize}
.hero-title .hl{color:var(--green);text-transform:uppercase}

/* why choose */
.features{left:220px;top:700px;width:760px;display:flex;justify-content:space-between}
.feature{width:130px;text-align:center;font-size:10.5px;line-height:1.5;color:var(--muted)}
.feature.strong{color:var(--ink);font-weight:600}
.feature .ring{width:76px;height:76px;border-radius:50%;border:3px solid var(--navy);background:var(--green);margin:0 auto 12px;display:flex;align-items:center;justify-content:center;box-shadow:inset 0 0 0 4px var(--white)}

/* banner */
.banner{left:156px;top:928px;width:888px;height:182px;border-radius:8px;overflow:hidden;background:var(--navy)}
.banner-text{left:518px;top:976px;font-family:'Oswald',sans-serif;font-weight:500;font-size:20px;line-height:1.45;color:var(--white)}
.banner-text .hl{color:var(--green)}

/* about */
.about-copy{left:156px;top:1408px;width:400px;color:var(--white);font-size:10.2px;line-height:1.6}
.about-copy p+p{margin-top:14px}

/* mouthguards */
.card{position:absolute;top:1910px;width:278px;height:335px;background:var(--white);border-radius:10px;box-shadow:0 4px 16px rgba(12,43,107,.14);overflow:hidden}
.card .img{height:199px}
.card h3{font-size:14px;font-weight:600;color:var(--navy);margin:24px 24px 8px;line-height:1.15}
.card ul{list-style:none;margin-left:24px;font-size:11px;line-height:1.45;color:var(--ink)}
.card li{position:relative;padding-left:14px}
.card li::before{content:"";position:absolute;left:0;top:5px;width:7px;height:7px;border-radius:50%;background:var(--green)}
.card p{font-size:10px;line-height:1.6;margin:0 60px 0 24px;color:var(--ink)}
.card .go{position:absolute;right:20px;top:250px;width:30px;height:30px;border-radius:50%;background:var(--green)}

/* process */
.step-label{position:absolute;font-family:'Oswald',sans-serif;font-weight:500;font-size:16px}
.step-note{position:absolute;font-size:8.6px;line-height:1.3;text-align:center;color:var(--white)}
.ready{left:0;top:2824px;width:1200px;text-align:center;color:var(--white);font-size:11px;line-height:1.45}
.ready strong{font-weight:600;font-size:11.5px}

/* faq */
.faq{position:absolute;left:288px;width:624px;background:var(--white);border-radius:6px;box-shadow:0 2px 10px rgba(12,43,107,.12);padding:0 16px;font-size:10.5px;font-weight:600;color:var(--ink)}
.faq .toggle{position:absolute;right:14px;width:16px;height:16px;border-radius:50%;background:var(--navy)}
.faq.open .q{color:var(--green)}
.faq.open .toggle{background:var(--green)}
.faq .a{font-size:9.5px;font-weight:400;line-height:1.6;margin-top:8px;color:var(--ink)}

/* footer */
.footer-brand{left:156px;top:4318px;color:var(--white);font-weight:700;line-height:1}
.footer-brand .name1{font-size:31px;letter-spacing:1px}
.footer-brand .name2{font-size:17px;letter-spacing:.6px;margin-top:2px}
.partner{left:176px;top:4403px;width:135px;height:44px;background:var(--white);border-radius:6px;display:flex;flex-direction:column;align-items:center;justify-content:center;color:var(--navy)}
.partner .pname{font-size:15px;font-weight:600;letter-spacing:1px}
.partner .pline{font-size:7px;margin-top:2px}
.foot-col{color:var(--white);font-size:10.5px;line-height:1.75}
.foot-col h4{font-size:13px;font-weight:600;color:var(--green);margin-bottom:6px}
.foot-col .row{display:flex;gap:9px;align-items:flex-start}
.foot-col .dot{flex:0 0 10px;height:10px;margin-top:5px;border-radius:2px;background:var(--green)}
.bottom-bar{left:0;top:4501px;width:1200px;height:24px;background:var(--green);color:var(--white);font-size:10px}
</style>
</head>
<body>

<!-- Header -->
<header class="site-header">
  <div class="brand"><div class="name">TARVEL<br>MOUTHGUARDS</div><div class="tag">Custom fit guards every smile</div></div>
  <nav class="nav">
    <span class="active">Home</span><span>Why Choose Us</span><span>About Us</span><span>Our Mouthguards</span><span>Our Gallery</span><span>Contact Us</span>
  </nav>
  <span class="nav-icon" style="left:871px"></span>
  <span class="nav-icon" style="left:907px"></span>
  <div class="btn dark quick">Quick Inquiry</div>
</header>

<!-- Hero -->
<svg class="abs" style="left:0;top:74px" width="1200" height="720" viewBox="0 0 1200 720" aria-hidden="true">
  <defs>
    <linearGradient id="heroPhoto" x1="0" y1="0" x2="1" y2="1">
      <stop offset="0" stop-color="#5e8b4a"/><stop offset=".45" stop-color="#8aa36a"/><stop offset="1" stop-color="#3f5f9e"/>
    </linearGradient>
  </defs>
  <rect width="1200" height="720" fill="var(--navy)"/>
  <path d="M480 0 H1200 V640 C900 520 700 500 520 480 C560 330 560 140 480 0Z" fill="url(#heroPhoto)"/>
  <path d="M0 648 C250 470 600 440 1200 540 V720 H0Z" fill="var(--green)"/>
  <path d="M0 720 C200 560 560 500 1200 620 V720Z" fill="var(--white)"/>
</svg>
<div class="photo" role="img" aria-label="Two smiling children in sports jerseys wearing colourful mouthguards, holding a football" style="left:560px;top:74px;width:640px;height:500px"></div>
<div class="abs hero-text">
  <div class="hero-brand">Tarvel<br>Mouthguards</div>
  <div class="hero-title">Custom-Made Sports<br><span class="hl">Mouthguards</span> In Perth<br><span class="hl">Protect Your Smile</span> With A<br>Comfortable, Professional Fit.</div>
</div>
<div class="btn light" style="left:144px;top:432px;width:122px;height:33px">Contact Now</div>

<!-- Why Choose Us -->
<h2 class="abs heading navy" style="left:0;top:630px;width:1200px;font-size:33px">Why Choose Us</h2>
<div class="abs features">
  <div class="feature"><div class="ring"><svg width="34" height="34" viewBox="0 0 34 34"><circle cx="17" cy="17" r="11" fill="none" stroke="#fff" stroke-width="3" stroke-dasharray="5 3"/><circle cx="17" cy="17" r="5" fill="none" stroke="#fff" stroke-width="2.5"/></svg></div>Professionally Made By A Qualified Dental Prosthetist</div>
  <div class="feature"><div class="ring"><svg width="34" height="34" viewBox="0 0 34 34"><path d="M7 8 V18 A10 10 0 0 0 27 18 V8" fill="none" stroke="#fff" stroke-width="3"/><path d="M13 8 V17 A4 4 0 0 0 21 17 V8" fill="none" stroke="#fff" stroke-width="2.5"/></svg></div>Custom Fit For Comfort, Protection, And Durability</div>
  <div class="feature"><div class="ring"><svg width="34" height="34" viewBox="0 0 34 34"><circle cx="17" cy="12" r="7" fill="none" stroke="#fff" stroke-width="2.5"/><circle cx="12" cy="21" r="7" fill="none" stroke="#fff" stroke-width="2.5"/><circle cx="22" cy="21" r="7" fill="none" stroke="#fff" stroke-width="2.5"/></svg></div>Wide Range Of Colours And Designs</div>
  <div class="feature"><div class="ring"><svg width="34" height="34" viewBox="0 0 34 34"><circle cx="11" cy="11" r="4" fill="#fff"/><circle cx="23" cy="11" r="4" fill="#fff"/><rect x="5" y="18" width="24" height="10" rx="3" fill="none" stroke="#fff" stroke-width="2.5"/></svg></div>Available For Kids, Teens, And Adults</div>
  <div class="feature strong"><div class="ring"><svg width="34" height="34" viewBox="0 0 34 34"><path d="M6 28 V15 L17 7 L28 15 V28Z" fill="none" stroke="#fff" stroke-width="2.5"/><rect x="14" y="19" width="6" height="9" fill="#fff"/></svg></div>Clinic And Mobile School/Club Visits Available</div>
</div>

<!-- Consult banner -->
<svg class="abs" style="left:0;top:850px" width="330" height="330" viewBox="0 0 330 330" aria-hidden="true">
  <path d="M-60 20 A200 200 0 0 1 300 90" fill="none" stroke="#e3e8f0" stroke-width="14"/>
</svg>
<div class="abs banner">
  <svg class="abs" style="left:0;top:0" width="888" height="182" viewBox="0 0 888 182" aria-hidden="true">
    <path d="M700 0 H888 V182 H700 C650 140 650 40 700 0Z" fill="var(--green)"/>
    <path d="M690 0 C640 40 640 140 690 182" fill="none" stroke="#fff" stroke-width="6"/>
  </svg>
</div>
<div class="photo" role="img" aria-label="Open hands holding a clear blue custom mouthguard" style="left:215px;top:918px;width:255px;height:200px;border-radius:48% 52% 40% 60%/55% 45% 55% 45%;background:linear-gradient(135deg,#c9a07f,#7b5c46 60%,#3a5a9a)"></div>
<div class="abs banner-text">Talk To Us About Our <span class="hl">“Gap Free”</span><br>Mouthguards For Eligible Private<br>Health Insurance Members.</div>
<div class="btn light" style="left:818px;top:1004px;width:123px;height:33px">Consult Now</div>

<!-- About -->
<svg class="abs" style="left:0;top:1160px" width="1200" height="670" viewBox="0 0 1200 670" aria-hidden="true">
  <defs>
    <linearGradient id="aboutPhoto" x1="0" y1="0" x2="1" y2="0">
      <stop offset="0" stop-color="var(--navy)" stop-opacity="0"/><stop offset=".35" stop-color="#3c6fb8"/><stop offset="1" stop-color="#8fa9d4"/>
    </linearGradient>
  </defs>
  <path d="M0 50 C400 80 800 40 1200 0 V600 C800 520 300 560 0 650Z" fill="var(--navy)"/>
  <path d="M560 45 C800 40 1000 20 1200 0 V600 C1000 560 800 560 560 580Z" fill="url(#aboutPhoto)"/>
</svg>
<div class="photo" role="img" aria-label="Close-up of colourful glitter and checkered custom mouthguards" style="left:620px;top:1200px;width:580px;height:560px;background:linear-gradient(140deg,rgba(160,190,230,.0),rgba(200,215,240,.35))"></div>
<h2 class="abs heading green" style="left:156px;top:1346px;font-size:33px;text-align:left">About Us</h2>
<div class="abs about-copy">
  <p>My Name Is Elsie, And I Am A Dental Prosthetist With Over 20 Years Of Experience In The Dental Field. I Hold A Diploma Of Dental Technology And An Advanced Diploma Of Dental Prosthetics, Which I Obtained At Coastal Institute Of Technology In 2011. At Tarvel Mouthguards (Inside My Westgate Denture Care Clinic), My Work Involves Designing And Making Custom-Fitted Sports Mouthguards For Athletes Of All Ages.</p>
  <p>The Goal Is Simple: Provide Mouthguards That Fit Well, Feel Comfortable, And Offer Reliable Protection On The Field, Court, Or In The Ring. Every Mouthguard Is Made Individually, With Close Attention To Detail, So That Players Can Focus On Their Performance Rather Than Worrying About Their Smile.</p>
</div>
<div class="btn light" style="left:156px;top:1617px;width:107px;height:33px">Read More</div>
<div class="abs" style="left:658px;top:1314px;width:342px;height:342px;border-radius:50%;background:var(--green);padding:9px">
  <div style="width:100%;height:100%;border-radius:50%;background:var(--white);padding:7px">
    <div class="photo" role="img" aria-label="Portrait of the dental prosthetist in a dark t-shirt" style="position:relative;width:100%;height:100%;border-radius:50%;background:radial-gradient(circle at 50% 40%,#6a6f78,#2b2e34 70%)"></div>
  </div>
</div>

<!-- Our Mouthguards -->
<svg class="abs" style="left:880px;top:2140px" width="320" height="220" viewBox="0 0 320 220" aria-hidden="true">
  <circle cx="220" cy="190" r="150" fill="#f1f6ee"/>
  <path d="M80 220 A150 150 0 0 1 320 70" fill="none" stroke="#e3e8f0" stroke-width="12"/>
</svg>
<h2 class="abs heading navy" style="left:0;top:1817px;width:1200px;font-size:33px">Our Mouthguards</h2>
<div class="abs" style="left:0;top:1864px;width:1200px;text-align:center;font-size:13px;font-weight:500">Protection, Comfort, Confidence</div>
<div class="card" style="left:156px">
  <div class="photo img" role="img" aria-label="Dental prosthetist fitting a mouthguard for a young patient in the clinic" style="position:relative;background:linear-gradient(135deg,#b8c6cf,#6d7f8c)"></div>
  <h3>Why Our Custom<br>Mouthguards?</h3>
  <ul><li>Maximum Protection</li><li>Superior Comfort</li><li>Durability</li></ul>
</div>
<div class="card" style="left:460px">
  <div class="photo img" role="img" aria-label="Smiling boy holding a blue mouthguard" style="position:relative;background:linear-gradient(135deg,#9a9590,#c9b27a 60%,#2f7fd0)"></div>
  <h3>Types Available</h3>
  <ul><li>Kid’s Mouthguards</li><li>Single-Layer</li><li>Double-Layer</li><li>Triple-Layer</li></ul>
</div>
<div class="card" style="left:766px">
  <div class="photo img" role="img" aria-label="Assorted patterned mouthguards on a blue background" style="position:relative;background:linear-gradient(135deg,#1f7ed6,#2f8fe0 50%,#1a64b8)"></div>
  <h3>Design Options</h3>
  <p>Design Your Own Mouthguard With A Choice Of Nearly 40 Colours Which You Can Mix And Match Into Different Styles. Choose From Team...</p>
  <span class="go"><svg width="30" height="30" viewBox="0 0 30 30"><path d="M13 9 L19 15 L13 21" fill="none" stroke="#fff" stroke-width="2.6"/></svg></span>
</div>
<div class="btn dark" style="left:538px;top:2286px;width:123px;height:33px">Consult Now</div>

<!-- Process -->
<svg class="abs" style="left:0;top:2350px" width="1200" height="760" viewBox="0 0 1200 760" aria-hidden="true">
  <defs>
    <linearGradient id="procBg" x1="0" y1="0" x2="1" y2="0.35">
      <stop offset="0" stop-color="#44d62c"/><stop offset=".4" stop-color="#1a7a4e"/><stop offset=".62" stop-color="var(--navy)"/><stop offset="1" stop-color="var(--navy)"/>
    </linearGradient>
    <linearGradient id="s1" x1="0" x2="1"><stop offset="0" stop-color="#ffd400"/><stop offset="1" stop-color="#f26b21"/></linearGradient>
    <linearGradient id="s2" x1="0" x2="1"><stop offset="0" stop-color="#f26b21"/><stop offset="1" stop-color="#2fb44a"/></linearGradient>
    <linearGradient id="s3" x1="0" x2="1"><stop offset="0" stop-color="#2fb44a"/><stop offset="1" stop-color="#1aa0e0"/></linearGradient>
    <linearGradient id="s4" x1="0" x2="1"><stop offset="0" stop-color="#1a8fe0"/><stop offset="1" stop-color="#f0406e"/></linearGradient>
  </defs>
  <path d="M0 30 C300 0 700 -20 1200 10 V640 C800 700 400 740 0 690Z" fill="url(#procBg)"/>
  <path d="M0 760 V720 C400 640 800 620 1200 660 V760Z" fill="#fff"/>
  <!-- serpentine -->
  <path d="M239 342 C239 210 400 210 410 300" fill="none" stroke="url(#s1)" stroke-width="6" stroke-linecap="round"/>
  <path d="M410 300 C420 440 600 440 605 340" fill="none" stroke="url(#s2)" stroke-width="6"/>
  <path d="M605 340 C610 210 780 210 785 300" fill="none" stroke="url(#s3)" stroke-width="6"/>
  <path d="M785 300 C790 440 970 440 970 342" fill="none" stroke="url(#s4)" stroke-width="6" stroke-linecap="round"/>
  <circle cx="239" cy="344" r="15" fill="#ffd400"/>
  <circle cx="970" cy="342" r="15" fill="#f0406e"/>
  <!-- icons -->
  <g fill="none" stroke="#ffc000" stroke-width="2.4"><rect x="312" y="326" width="32" height="28" rx="3"/><line x1="312" y1="335" x2="344" y2="335"/><line x1="320" y1="321" x2="320" y2="329"/><line x1="336" y1="321" x2="336" y2="329"/></g>
  <g fill="none" stroke="#3fd14a" stroke-width="2.4"><circle cx="511" cy="340" r="15"/><path d="M503 336 C510 344 514 344 520 334"/></g>
  <path d="M680 323 V338 A14 14 0 0 0 708 338 V323 M687 323 V337 A7 7 0 0 0 701 337 V323" fill="none" stroke="#1a8fe0" stroke-width="2.4"/>
  <g fill="none" stroke="#f0406e" stroke-width="2.4"><path d="M855 330 H885 V352 H855Z"/><path d="M862 330 V322 H878 V330"/></g>
</svg>
<h2 class="abs heading green" style="left:0;top:2503px;width:1200px;font-size:33px">The Process</h2>
<span class="step-label" style="left:305px;top:2628px;color:#f58a22">1 Step</span>
<span class="step-label" style="left:490px;top:2729px;color:#3fd14a">2 Step</span>
<span class="step-label" style="left:672px;top:2628px;color:#1aa0e0">3 Step</span>
<span class="step-label" style="left:855px;top:2731px;color:#f0406e">4 Step</span>
<div class="step-note" style="left:255px;top:2732px;width:140px">Book An Appointment Or Mobile Visit With Our Dental Prosthetist.</div>
<div class="step-note" style="left:430px;top:2592px;width:150px">Impressions Are Taken Of The Mouth – This Appointment Will Generally Take Around 15 Minutes. You Then Get To Choose Your Design (If You Haven’t Already!)</div>
<div class="step-note" style="left:625px;top:2732px;width:140px">Mouthguard Is Made In-House In Our Laboratory By Our Prosthetist And Technicians.</div>
<div class="step-note" style="left:800px;top:2592px;width:150px">Fit And Collection – You May Either Pick Up From Our Clinic Or For Sporting Clubs Or Schools, We Can Have Them Packed And Delivered To You.</div>
<div class="abs ready"><strong>Now You’re Ready For Game Day!</strong><br>Our Turnaround Time Is Generally 1-2 Weeks. However We May Be Able To Accommodate<br>Quicker Turnaround Times. Contact Us For More Details.</div>
<div class="btn light" style="left:545px;top:2887px;width:103px;height:32px">Book Now</div>

<!-- Gallery -->
<h2 class="abs heading green" style="left:0;top:3120px;width:1200px;font-size:33px">Our Gallery</h2>
<div class="photo" role="img" aria-label="Girl in a sports jersey smiling with an orange mouthguard" style="left:156px;top:3273px;width:202px;height:225px;border-radius:6px;background:linear-gradient(135deg,#6f9a52,#4f3f8e)"></div>
<div class="photo" role="img" aria-label="Child holding a pink mouthguard up to the camera" style="left:385px;top:3194px;width:202px;height:144px;border-radius:6px;background:linear-gradient(135deg,#e2b9a5,#f07f8a)"></div>
<div class="photo" role="img" aria-label="Boy holding a blue mouthguard" style="left:385px;top:3365px;width:202px;height:203px;border-radius:6px;background:linear-gradient(135deg,#a09a92,#d5b45c 60%,#2f7fd0)"></div>
<div class="photo" role="img" aria-label="Hand holding a blue patterned mouthguard" style="left:611px;top:3194px;width:204px;height:206px;border-radius:6px;background:linear-gradient(135deg,#e6edf4,#3c7ed6)"></div>
<div class="photo" role="img" aria-label="Pile of checkered and glitter mouthguards" style="left:611px;top:3426px;width:204px;height:142px;border-radius:6px;background:linear-gradient(135deg,#7fb3d8,#e68aa0 55%,#4c6fc0)"></div>
<div class="photo" role="img" aria-label="Boy holding a football wearing a green mouthguard" style="left:842px;top:3273px;width:202px;height:225px;border-radius:6px;background:linear-gradient(135deg,#5e8b4a,#c9a84a 55%,#2f4f9e)"></div>
<div class="btn dark" style="left:555px;top:3601px;width:91px;height:31px">View All</div>

<!-- FAQs -->
<svg class="abs" style="left:0;top:3660px" width="1200" height="560" viewBox="0 0 1200 560" aria-hidden="true">
  <defs><linearGradient id="faqBg" x1="0" y1="0" x2="1" y2="0"><stop offset="0" stop-color="#eef7ea"/><stop offset="1" stop-color="#e8eef6"/></linearGradient></defs>
  <path d="M0 60 C400 0 800 0 1200 50 V560 H0Z" fill="url(#faqBg)"/>
</svg>
<h2 class="abs heading green" style="left:0;top:3824px;width:1200px;font-size:33px">FAQs</h2>
<div class="faq open" style="top:3888px;height:80px;padding-top:12px">
  <div class="q">How Long Does A Mouthguard Last?</div>
  <span class="toggle" style="top:11px"></span>
  <div class="a">1-2 Years For Adults. Children Generally Will Need A New Fitting Each Year As Their Teeth And Size Of Their Mouths<br>Are Changing Month To Month.</div>
</div>
<div class="faq" style="top:3978px;height:32px;line-height:32px"><div class="q">Are Mouthguards Covered By Health Funds?</div><span class="toggle" style="top:8px"></span></div>
<div class="faq" style="top:4022px;height:32px;line-height:32px"><div class="q">Why Not Buy A Mouthguard From The Chemist?</div><span class="toggle" style="top:8px"></span></div>
<div class="faq" style="top:4066px;height:32px;line-height:32px"><div class="q">Do You Visit Schools And Clubs?</div><span class="toggle" style="top:8px"></span></div>
<div class="btn dark" style="left:555px;top:4135px;width:91px;height:31px">View All</div>

<!-- Footer -->
<svg class="abs" style="left:0;top:4150px" width="1200" height="375" viewBox="0 0 1200 375" aria-hidden="true">
  <path d="M0 110 C400 40 800 30 1200 60 V375 H0Z" fill="var(--green)"/>
  <path d="M0 126 C400 60 800 52 1200 82 V375 H0Z" fill="var(--navy)"/>
</svg>
<div class="abs" style="left:780px;top:4212px;width:362px;height:362px;border-radius:50%;background:var(--white);padding:8px">
  <div class="photo" role="img" aria-label="Street map showing the clinic location" style="position:relative;width:100%;height:100%;border-radius:50%;background:linear-gradient(135deg,#eef0f2,#dfe3e8)"></div>
</div>
<div class="abs footer-brand"><div class="name1">TARVEL</div><div class="name2">MOUTHGUARDS</div></div>
<div class="abs partner"><span class="pname">MORVEX</span><span class="pline">Fast claims on the spot</span></div>
<div class="abs foot-col" style="left:406px;top:4314px;width:190px">
  <h4>Contact Us</h4>
  <div class="row"><span class="dot"></span><span>(08) 6100 2735</span></div>
  <div class="row"><span class="dot"></span><span>info@tarvelmouthguards.com.au</span></div>
  <div class="row"><span class="dot"></span><span>Unit 3, 12 Harlow Crescent, Brenton, Western Australia, 6091</span></div>
</div>
<div class="abs foot-col" style="left:613px;top:4314px;width:140px">
  <h4>Quick Links</h4>
  <div style="color:var(--green)">Home</div><div>Why Choose Us</div><div>About Us</div><div>Our Mouthguards</div><div>Our Gallery</div><div>Contact Us</div>
</div>
<div class="abs bottom-bar">
  <span class="abs" style="left:148px;top:5px">© 2025 <strong>Tarvel Mouthguard,</strong> All Rights Reserved. &nbsp;&nbsp;&nbsp; Privacy Policy</span>
  <span class="abs" style="left:966px;top:6px;width:11px;height:11px;background:var(--white);border-radius:2px"></span>
  <span class="abs" style="left:996px;top:6px;width:11px;height:11px;background:var(--white);border-radius:2px"></span>
  <span class="abs" style="left:1025px;top:3px;width:18px;height:18px;background:var(--white);border-radius:50%"></span>
</div>

</body>
</html>
```